Brightwave Audiology Letterhead redesign project

We need a full redesign of our current letterhead to make it consistent with the look and feel of our website design www.brightwaveaudio.com.au. It will need to include all information on the current version attached. The letterhead is used for sending medical reports and general correspondence. It should make use of our corporate colours (purple and teal) as per the logo on the existing file. The letterhead should be bold and eye-catching.

Target Market(s)

Medical practitioners.

Font styles to use
Sans Serif

Requirements
Must have
• It will need to include all information on the current version. Must have a premium, professional, high-end look and feel.
Nice to have
• Bold and eye-catching letterhead that reinforces the Brightwave Audiology brand. To stand out from other traditional letterheads.
Should not have
• The design should not be too cluttered or 'busy'

```html
<!DOCTYPE html>
<html lang="en">
<head>
<meta charset="utf-8">
<title>Brightwave Audiology Letterhead</title>
<link href="https://fonts.googleapis.com/css2?family=Roboto:wght@400;700;900&display=swap" rel="stylesheet">
<style>
  :root {
    --brand-purple: #7a2a90;
    --brand-teal: #13a98a;
    --ink: #6d6d6d;
    --ink-dark: #4a4a4a;
    --paper: #ffffff;
    --backdrop: #ebebeb;
  }
  * { margin: 0; padding: 0; box-sizing: border-box; }
  html, body { width: 1200px; height: 866px; overflow: hidden; background: var(--backdrop); }
  body { font-family: 'Roboto', Arial, sans-serif; color: var(--ink); }

  .letterhead {
    position: absolute; left: 303px; top: 18px;
    width: 593px; height: 830px;
    background: var(--paper);
  }

  .brand { position: absolute; left: 50px; top: 48px; }
  .brand-name {
    font-weight: 900; font-size: 27px; line-height: 1.05;
    color: var(--brand-purple); letter-spacing: -0.5px;
  }

  .contact {
    position: absolute; left: 408px; top: 45px;
    border-left: 1.5px solid var(--brand-teal);
    padding-left: 12px; height: 80px;
    font-size: 9.5px; line-height: 13.6px; color: var(--ink-dark);
    font-style: normal;
  }
  .contact .address { margin-bottom: 3px; }
  .contact li { list-style: none; display: flex; align-items: center; gap: 4px; }
  .contact svg { width: 9px; height: 9px; fill: var(--brand-purple); flex: none; }

  .recipient {
    position: absolute; left: 50px; top: 250px;
    font-size: 11px; line-height: 15.4px;
  }

  .letter-body {
    position: absolute; left: 50px; top: 342px; width: 492px;
    font-size: 10.6px; line-height: 15.4px; text-align: justify;
  }
  .letter-body p + p { margin-top: 30px; }

  .signature {
    position: absolute; left: 50px; top: 566px;
    width: 115px; height: 72px;
    background: linear-gradient(135deg, #efe6f2, #e3d3e9);
    border-radius: 4px;
  }
  .signatory {
    position: absolute; left: 49px; top: 652px; font-size: 11px;
  }

  .footer-band { position: absolute; left: 0; bottom: 0; width: 593px; height: 13px; display: block; }
</style>
</head>
<body>
  <main class="letterhead">
    <header class="brand">
      <div class="brand-name">Brightwave<br>Audiology</div>
    </header>

    <address class="contact">
      <div class="address">48 Carrow Lane, Harlow Vale<br>Qld 4361</div>
      <ul>
        <li><svg viewBox="0 0 10 10"><path d="M2 0.5 L3.8 0.5 L4.4 3 L3.2 3.8 Q4.2 6 6.2 6.8 L7 5.6 L9.5 6.2 L9.5 8 Q9.5 9.5 8 9.5 Q0.5 9 0.5 2 Q0.5 0.5 2 0.5Z"/></svg>07 5100 2841</li>
        <li><svg viewBox="0 0 10 10"><rect x="2.5" y="0.5" width="5" height="2.5"/><rect x="0.5" y="3.5" width="9" height="4" rx="1"/><rect x="2.5" y="6.5" width="5" height="3"/></svg>07 5100 2842</li>
        <li><svg viewBox="0 0 10 10"><rect x="0.5" y="2" width="9" height="6.5" rx="0.8"/><path d="M0.8 2.4 L5 5.6 L9.2 2.4" stroke="#fff" stroke-width="0.9" fill="none"/></svg>hello@brightwaveaudio.com.au</li>
        <li><svg viewBox="0 0 10 10"><circle cx="5" cy="5" r="4.5"/><path d="M0.5 5 H9.5 M5 0.5 Q2.5 5 5 9.5 M5 0.5 Q7.5 5 5 9.5" stroke="#fff" stroke-width="0.7" fill="none"/></svg>www.brightwaveaudio.com.au</li>
      </ul>
    </address>

    <section class="recipient">
      Dear Marlowe<br>
      Northgate Clinical Group<br>
      Department Design
    </section>

    <section class="letter-body">
      <p>Lorem ipsum dolor sit amet, consectetuer adipiscing elit. Aenean commodo ligula eget dolor. Aenean massa. Cum sociis natoque penatibus et magnis dis parturient montes, nascetur ridiculus mus. Donec quam felis, ultricies nec, pellentesque eu, pretium quis, sem. Nulla consequat massa quis enim. Donec pede justo, fringilla vel, aliquet nec, vulputate eget, arcu. In enim justo, rhoncus ut, imperdiet a, venenatis vitae, justo. Nullam dictum felis eu pede mollis pretium. Integer tincidunt. Cras dapibus. Vivamus elementum semper nisi.Nullam dictum felis eu pede mollis pretium. Integer tincidunt. Cras dapibus. Vivamus elementum semper nisi.felis eu pede mollis pretium. Integer tincidunt. Cras dapibus.</p>
      <p>Quisque rutrum. Aenean imperdiet. Etiam ultricies nisi vel augue. Curabitur ullamcorper ultricies nisi. Nam eget dui. Etiam rhoncus. Maecenas tempus, tellus eget condimentum rhoncus, sem quam semper libero, sit amet adipiscing sem neque sed ipsum.felis pede mollis pretium. I am tincidunt. Cras dapibus.</p>
    </section>

    <div class="signature" role="img" aria-label="Handwritten signature of the director"></div>
    <div class="signatory">Director/Excecutive Director</div>

    <svg class="footer-band" viewBox="0 0 593 13" preserveAspectRatio="none" aria-hidden="true">
      <polygon points="0,0 357,0 365,13 0,13" fill="var(--brand-purple)"/>
      <polygon points="363,0 593,0 593,13 371,13" fill="var(--brand-teal)"/>
    </svg>
  </main>
</body>
</html>
```